Physician focused educational website needed

We are looking to create a fresh, simple website to help Physicians understand the benefits of protecting their largest asset....their income. We are wanting to create a site that can be a resource to help answer the FAQ that physicians ask regarding Disability Insurance. The goal is not to sell DI but rather to education the physician on the importance of the product and to be a resource for them to learn more.

Target Market(s)

Physicians

Industry/Entity Type

Insurance

Coding

Coded - Design and coding required

Number of Pages Required

1 page

Requirements
Must have
• easy to navigate and understand FAQ format

```html
<!DOCTYPE html>
<html lang="en">
<head>
<meta charset="utf-8">
<title>ShieldRx Income — Income Protection Insurance for Physicians</title>
<link href="https://fonts.googleapis.com/css2?family=Open+Sans:ital,wght@0,400;0,600;0,700;1,400;1,600;1,700&display=swap" rel="stylesheet">
<style>
:root{
  --brand:#3b6b8f;
  --brand-dark:#2f5b7c;
  --ink:#333b44;
  --muted:#6b7279;
  --line:#e3e6e9;
  --footer-bg:#efefef;
  --bar-bg:#f6f6f6;
  --white:#ffffff;
}
*{box-sizing:border-box;margin:0;padding:0}
html,body{width:1200px;height:2804px;overflow:hidden}
body{font-family:"Open Sans",Arial,sans-serif;color:var(--ink);background:var(--white)}
.wrap{width:976px;margin:0 auto;position:relative}

/* header */
.site-header{height:120px}
.site-header .wrap{height:120px;display:flex;align-items:center;justify-content:space-between}
.brand{font-family:"Open Sans",Arial,sans-serif;font-weight:600;font-size:32px;color:var(--brand);letter-spacing:-.3px}
.main-nav{display:flex;align-items:center}
.main-nav a{font-size:13px;font-weight:600;color:var(--ink);text-decoration:none;margin-left:64px}
.main-nav a.active{color:var(--brand)}
.btn-signup{display:inline-flex;align-items:center;gap:6px;background:var(--brand);color:var(--white)!important;border-radius:22px;padding:11px 22px;margin-left:40px!important}

/* hero */
.hero{height:503px;position:relative;overflow:hidden;
  background:linear-gradient(90deg,#e9eef0 0%,#dde6e8 30%,#eef1f2 55%,#f7f8f8 100%)}
.hero-photo{position:absolute;right:0;top:0;width:470px;height:503px;
  background:linear-gradient(160deg,#f3f4f5 0%,#e7ecef 45%,#c9d6de 100%)}
.hero .wrap{padding-top:162px}
.hero-title{font-style:italic;font-weight:600;font-size:60px;color:var(--brand);line-height:1.1}
.hero-sub{font-style:italic;font-weight:400;font-size:32px;color:var(--ink);margin-top:8px}
.btn-outline{display:inline-flex;align-items:center;gap:10px;border:1.5px solid var(--brand);color:var(--brand);
  border-radius:30px;height:58px;padding:0 50px;font-size:14px;font-weight:600;text-decoration:none;margin-top:42px}
.hero-dots{position:absolute;left:0;right:0;bottom:36px;display:flex;justify-content:center;gap:10px}
.hero-dots span{width:11px;height:11px;border-radius:50%;background:#b9c1c6}
.hero-dots span.on{background:var(--brand)}

/* welcome */
.welcome{height:405px}
.welcome .wrap{display:flex;justify-content:space-between;padding-top:85px}
.welcome-text{width:610px}
.section-title{font-style:italic;font-weight:400;font-size:32px;color:var(--ink)}
.section-title b{font-weight:700}
.welcome-text p{font-size:11px;line-height:25px;color:var(--muted);margin-top:24px}
.team-art{width:340px;height:245px;margin-top:-2px;border-radius:6px;
  background:radial-gradient(ellipse at 50% 60%,#3f7fc0 0%,#2f6aa6 45%,#dfe8f0 72%,#ffffff 100%)}

/* band */
.band{height:250px;background:var(--brand);text-align:center;padding-top:60px}
.band-text{font-style:italic;font-size:24px;color:var(--white)}
.band .btn-outline{border-color:var(--white);color:var(--white);margin-top:38px;padding:0 52px}

/* faq */
.faq{height:1005px;padding-top:88px}
.faq .section-title{text-align:center;font-weight:700;font-size:32px}
.faq-list{margin-top:32px}
.faq-item{border-bottom:1px solid var(--line);padding:22px 0}
.faq-item:first-child{padding-top:0}
.faq-q{display:flex;align-items:center;font-size:14px;color:var(--ink);height:42px}
.q-mark{flex:none;width:32px;height:32px;border-radius:50%;background:var(--brand);color:var(--white);
  font-weight:700;font-size:14px;display:flex;align-items:center;justify-content:center;margin-right:16px}
.faq-q .txt{flex:1}
.toggle{flex:none;width:18px;height:18px}
.faq-a{font-size:11.5px;line-height:27px;color:var(--muted);margin-top:18px}

/* footer */
.site-footer{height:438px;background:var(--footer-bg)}
.site-footer .wrap{display:flex;padding-top:88px}
.foot-about{width:420px}
.foot-about .brand{font-size:40px}
.foot-about p{font-size:11px;line-height:22px;color:var(--muted);width:345px;margin-top:16px}
.contact-row{display:flex;align-items:center;gap:16px;margin-top:24px;font-size:11px;color:var(--muted);line-height:20px}
.contact-row b{color:var(--ink);font-weight:600}
.foot-links{width:270px}
.foot-title{font-style:italic;font-weight:400;font-size:20px;color:var(--ink);margin-top:6px}
.foot-title b{font-weight:600}
.foot-links ul{list-style:none;margin-top:22px}
.foot-links li{font-size:11px;color:var(--muted);line-height:34px}
.foot-links li::before{content:"›";margin-right:8px}
.foot-news{width:286px}
.foot-news p{font-size:11px;line-height:24px;color:var(--muted);margin-top:24px}
.news-form{margin-top:22px;display:flex;border:1px solid #d6d9dc;background:var(--white);height:46px;padding:4px}
.news-form input{flex:1;border:0;outline:0;font-family:inherit;font-style:italic;font-size:11px;padding-left:18px;color:var(--muted);background:transparent}
.news-form button{width:50px;border:0;background:var(--brand);display:flex;align-items:center;justify-content:center}

/* bottom bar */
.bottom-bar{height:83px;background:var(--bar-bg)}
.bottom-bar .wrap{height:83px;display:flex;align-items:center;justify-content:space-between}
.copyright{font-size:11px;color:var(--muted)}
.social{display:flex;gap:10px}
.social span{width:28px;height:28px;border-radius:50%;background:#e2e4e6}
</style>
</head>
<body>

<header class="site-header">
  <div class="wrap">
    <div class="brand">ShieldRx Income</div>
    <nav class="main-nav">
      <a class="active" href="#">HOME</a>
      <a href="#">ABOUT</a>
      <a href="#">FAQ</a>
      <a href="#">CONTACT US</a>
      <a class="btn-signup" href="#">
        <svg width="11" height="12" viewBox="0 0 11 12"><circle cx="5.5" cy="3.2" r="2.8" fill="#fff"/><path d="M0 12c0-3.3 2.4-5 5.5-5s5.5 1.7 5.5 5z" fill="#fff"/></svg>
        SIGN UP</a>
    </nav>
  </div>
</header>

<section class="hero">
  <div class="hero-photo" role="img" aria-label="Smiling physician in a white coat with a stethoscope holding a clipboard"></div>
  <div class="wrap">
    <h1 class="hero-title">ShieldRx Income</h1>
    <p class="hero-sub">Income Protection Insurance for Physicians</p>
    <a class="btn-outline" href="#">NEED MORE INFORMATION
      <svg width="14" height="10" viewBox="0 0 14 10"><path d="M0 5h12M8 1l4 4-4 4" stroke="currentColor" stroke-width="1.8" fill="none"/></svg></a>
  </div>
  <div class="hero-dots"><span></span><span class="on"></span><span></span><span></span></div>
</section>

<section class="welcome">
  <div class="wrap">
    <div class="welcome-text">
      <h2 class="section-title">Welcome To <b>ShieldRx Income</b></h2>
      <p>Donec volutpat urna vel consectetur elementum. Nam ultricies porttitor nisl, ut bibendum tellus suscipit vel. Vivamus feugiat magna ut suscipit ornare. Donec nec aliquet tellus. Curabitur dignissim felis at arcu aliquam consectetur. Morbi tincidunt aliquam augue, ut finibus neque ullamcorper eleifend. Suspendisse tincidunt, dolor in ornare ultricies, lacus libero tincidunt est, id sodales metus nibh vitae turpis. Sed at nunc arcu. Integer id interdum ante, eget ullamcorper lacus. Aliquam at velit a odio sollicitudin rhoncus at accumsan dolor. Suspendisse maximus rhoncus ante, vitae posuere risus commodo rutrum.</p>
    </div>
    <div class="team-art" role="img" aria-label="Illustration of a group of medical staff in blue scrubs"></div>
  </div>
</section>

<section class="band">
  <p class="band-text">We help Physicians understand the benefits of protecting their largest asset....their income</p>
  <a class="btn-outline" href="#">NEED MORE INFORMATION
    <svg width="14" height="10" viewBox="0 0 14 10"><path d="M0 5h12M8 1l4 4-4 4" stroke="currentColor" stroke-width="1.8" fill="none"/></svg></a>
</section>

<section class="faq">
  <div class="wrap">
    <h2 class="section-title">FAQs</h2>
    <div class="faq-list">
      <div class="faq-item">
        <div class="faq-q"><span class="q-mark">?</span><span class="txt">When is the right time to buy Income Protection plan/should I buy while in training/Is there an advantage to buying as a PGY 1?</span>
          <svg class="toggle" viewBox="0 0 18 18"><circle cx="9" cy="9" r="9" fill="#6b7279"/><rect x="4.5" y="8" width="9" height="2" fill="#fff"/></svg></div>
        <div class="faq-a">
          The right time to buy insurance is today.&nbsp; Our health can change in an instant so buying coverage while you are young and healthy is imperative.&nbsp; Even as a PGY1, locking in your insurability is important.&nbsp; As more and more residents are starting to take medications for stress and anxiety during these difficult years, your ability to get insurance can be drastically impacted by something that “everyone is doing” just to get by.<br>
          What matters is that you obtain some form of coverage with the ability to purchase more later regardless of your health.&nbsp; At the very latest, you should make sure you are securing coverage before leaving your training program because you receive significant discounts while in training that you won’t be able to get once you leave.
        </div>
      </div>
      <div class="faq-item"><div class="faq-q"><span class="q-mark">?</span><span class="txt">Wouldn’t my group coverage cover me adequately? (what is the difference between group/private)</span>
        <svg class="toggle" viewBox="0 0 18 18"><circle cx="9" cy="9" r="9" fill="#6b7279"/><path d="M4.5 8h9v2h-9zM8 4.5h2v9H8z" fill="#fff"/></svg></div></div>
      <div class="faq-item"><div class="faq-q"><span class="q-mark">?</span><span class="txt">What features should I look for?</span>
        <svg class="toggle" viewBox="0 0 18 18"><circle cx="9" cy="9" r="9" fill="#6b7279"/><path d="M4.5 8h9v2h-9zM8 4.5h2v9H8z" fill="#fff"/></svg></div></div>
      <div class="faq-item"><div class="faq-q"><span class="q-mark">?</span><span class="txt">What is true own occupation/specialty specific mean?</span>
        <svg class="toggle" viewBox="0 0 18 18"><circle cx="9" cy="9" r="9" fill="#6b7279"/><path d="M4.5 8h9v2h-9zM8 4.5h2v9H8z" fill="#fff"/></svg></div></div>
      <div class="faq-item"><div class="faq-q"><span class="q-mark">?</span><span class="txt">What is Catastrophic Benefit?</span>
        <svg class="toggle" viewBox="0 0 18 18"><circle cx="9" cy="9" r="9" fill="#6b7279"/><path d="M4.5 8h9v2h-9zM8 4.5h2v9H8z" fill="#fff"/></svg></div></div>
      <div class="faq-item"><div class="faq-q"><span class="q-mark">?</span><span class="txt">What is DIRS? (disability income retirement supplement)</span>
        <svg class="toggle" viewBox="0 0 18 18"><circle cx="9" cy="9" r="9" fill="#6b7279"/><path d="M4.5 8h9v2h-9zM8 4.5h2v9H8z" fill="#fff"/></svg></div></div>
      <div class="faq-item"><div class="faq-q"><span class="q-mark">?</span><span class="txt">What if my health changes after I buy coverage?</span>
        <svg class="toggle" viewBox="0 0 18 18"><circle cx="9" cy="9" r="9" fill="#6b7279"/><path d="M4.5 8h9v2h-9zM8 4.5h2v9H8z" fill="#fff"/></svg></div></div>
    </div>
  </div>
</section>

<footer class="site-footer">
  <div class="wrap">
    <div class="foot-about">
      <div class="brand">ShieldRx Income</div>
      <p>Donec vel arcu risus. Sed varius id eros ut commodo. Sed auctor, erat eu pharetra tincid unt, urna massa</p>
      <div class="contact-row">
        <svg width="24" height="36" viewBox="0 0 24 36"><rect x="2" y="1.5" width="20" height="33" rx="3" fill="none" stroke="#3b6b8f" stroke-width="1.8"/><path d="M2 7h20M2 28h20" stroke="#3b6b8f" stroke-width="1.5"/><circle cx="12" cy="31.2" r="1.3" fill="#3b6b8f"/></svg>
        <div><b>555-014-27360</b><br>hello@shieldrxincome.com</div>
      </div>
      <div class="contact-row">
        <svg width="34" height="36" viewBox="0 0 34 36"><path d="M17 26S8 16 8 10a9 9 0 0 1 18 0c0 6-9 16-9 16z" fill="none" stroke="#3b6b8f" stroke-width="1.8"/><circle cx="17" cy="10" r="3.2" fill="none" stroke="#3b6b8f" stroke-width="1.6"/><path d="M9 24l-7 10h30l-7-10" fill="none" stroke="#3b6b8f" stroke-width="1.6"/></svg>
        <div><b>18 Harbor Row</b><br>Westbrook, NR4 7QD</div>
      </div>
    </div>
    <div class="foot-links">
      <h3 class="foot-title">Quick <b>Links</b></h3>
      <ul><li>About Us</li><li>About Us</li><li>FAQs</li><li>Contact Us</li><li>Privacy Policy</li><li>Sitemap</li></ul>
    </div>
    <div class="foot-news">
      <h3 class="foot-title">Newsletter <b>Signup</b></h3>
      <p>Vestibulum et libero ac quam varius tristique nec eu lacus. Proin lacus dolor, efficitur sit amet luctus at, euismod sit amet lectus.</p>
      <form class="news-form"><input type="text" placeholder="Email Address"><button type="button" aria-label="Subscribe">
        <svg width="16" height="14" viewBox="0 0 16 14"><path d="M0 7h13M8 1.5L13.5 7 8 12.5" stroke="#fff" stroke-width="2.4" fill="none"/></svg></button></form>
    </div>
  </div>
</footer>

<div class="bottom-bar">
  <div class="wrap">
    <p class="copyright">Copyright © 2016 shieldrxincome. All Right Reserved.</p>
    <div class="social" aria-label="Social links"><span></span><span></span><span></span><span></span><span></span></div>
  </div>
</div>

</body>
</html>
```